Revamp Current Website From 2012 TO 2018

We need a ravamp to our current website. I prefer a professional corporate modern feel to it.

My Current Website is www.brightlanepromoworks.biz. Please redesign the homepage and the /certs page first....see attached document for specific instructions..

There is a lot of content at the bottom but maybe we can shorten that by using titles and a pop up of the details or something so it doesnt take too mcuh space...or maybe a red more hyperlink to see the rest of info in pop up or something or new page...

Target Market(s)

B2B, business owners, website owners, marketing companies.

Industry/Entity Type

Promotional Product

Number of Pages Required

2 page

Colors

Designer to choose colors to be used in the design.

Requirements
Must have
• Please keep in mind logo mock up I am working on that looks beautiful on dark background for header...see attached for logo
• Must use existing content I hope your marketing mind comes in to play when designing the website.
• Must have all my content provided on each page...
Nice to have
• similiar color scheme...
Should not have
• I dont like using templates because usually hard to expand on design in future so Prefer full custom designs
• Please no templates

```html
<!DOCTYPE html>
<html lang="en">
<head>
<meta charset="utf-8">
<title>Brightlane Promoworks</title>
<link href="https://fonts.googleapis.com/css2?family=Poppins:wght@400;500;600;700&display=swap" rel="stylesheet">
<style>
:root{
  --blue:#0a7fdc;
  --blue-tint:#d6e9f8;
  --ink:#151515;
  --text:#444;
  --light:#f4f4f4;
  --white:#fff;
  --footer:#121212;
  --footer-bar:#0a0a0a;
}
*{box-sizing:border-box;margin:0;padding:0}
html,body{width:1200px;height:3991px;overflow:hidden}
body{font-family:'Poppins',sans-serif;color:var(--text);background:var(--white);position:relative}
.btn-dark{position:absolute;background:var(--ink);color:var(--white);font-weight:600;font-size:14px;display:flex;align-items:center;justify-content:center;border-radius:4px}
.btn-dark.sm{font-size:10px;width:90px;height:28px;border-radius:3px}

/* hero */
.hero{position:absolute;left:0;top:0;width:1200px;height:617px;background:linear-gradient(120deg,#2a2f36 0%,#4a5058 40%,#3a3c40 70%,#23252a 100%);overflow:hidden}
.hero-photo{position:absolute;inset:0;background:radial-gradient(ellipse at 45% 55%,rgba(110,120,130,.55),rgba(20,22,26,.1) 70%)}
.topbar{position:absolute;top:14px;right:120px;font-size:9px;color:#ddd;letter-spacing:.3px;display:flex;gap:24px}
.topbar b{color:var(--white);font-weight:600}
.nav{position:absolute;top:0;left:0;width:1200px;height:93px;background:rgba(10,12,16,.55)}
.logo{position:absolute;display:flex;align-items:center;gap:8px;color:var(--blue);font-weight:700;font-size:15px;letter-spacing:.5px}
.logo i{width:14px;height:14px;background:var(--blue);display:block}
.menu{position:absolute;top:42px;left:495px;display:flex;gap:22px;font-size:10px;font-weight:600;color:var(--white);letter-spacing:.3px;align-items:center}
.menu .active{color:var(--blue)}
.menu .login{border:1.5px solid var(--white);padding:5px 12px;border-radius:3px}
.stats{position:absolute;left:212px;top:226px;list-style:none;color:var(--white);font-size:11.5px;font-weight:600;line-height:22px}
.stats li:before{content:"";display:inline-block;width:5px;height:5px;background:var(--white);border-radius:50%;margin-right:10px;vertical-align:middle}
.badge{position:absolute;left:212px;top:346px;width:70px;height:36px;background:#e9e9e9;border-radius:2px}
.license{position:absolute;left:212px;top:394px;color:#ddd;font-size:10.5px}
.btn-blue{position:absolute;background:var(--blue);color:var(--white);font-weight:600;font-size:13px;display:flex;align-items:center;justify-content:center;border-radius:4px;letter-spacing:.4px}
.signup{position:absolute;left:752px;top:180px;width:260px;height:364px;border:2px solid var(--white);border-radius:4px;padding:20px 20px}
.signup h3{color:var(--white);font-size:18px;font-weight:700;line-height:24px;margin-bottom:18px}
.field{height:34px;border:1.5px solid rgba(255,255,255,.8);border-radius:3px;margin-bottom:11px;color:var(--white);font-size:11px;padding:0 10px;display:flex;align-items:center}
.signup .btn-blue{position:static;height:34px;font-size:11px;margin-top:6px}
.side-tab{position:absolute;right:0;top:175px;width:40px;height:108px;background:var(--blue);color:var(--white);font-size:13px;font-weight:700;letter-spacing:1px;writing-mode:vertical-rl;display:flex;align-items:center;justify-content:center;border-radius:4px 0 0 4px}
.dots{position:absolute;display:flex;gap:10px}
.dots span{width:8px;height:8px;border-radius:50%;background:var(--white)}
.dots .on{background:var(--blue)}

/* intro */
.intro-title{position:absolute;left:205px;top:676px;width:375px;color:var(--blue);font-weight:700;font-size:20px;line-height:30px}
.intro-text{position:absolute;left:205px;top:826px;width:400px;font-size:13.5px;line-height:23px;color:var(--text)}
.ph{position:absolute}
.intro-photo{left:637px;top:685px;width:378px;height:353px;background:linear-gradient(150deg,#8a6a4c 0%,#b08864 35%,#7d8a94 70%,#5c4a3a 100%)}

/* band */
.band{position:absolute;left:0;top:1099px;width:1200px;height:152px;background:var(--blue);color:var(--white);font-size:28px;font-weight:700;text-align:center;line-height:42px;padding-top:32px}

/* ways */
.way-title{position:absolute;color:var(--blue);font-weight:700;font-size:14px;line-height:23px}
.way-text{position:absolute;font-size:11.5px;line-height:19px;color:var(--text)}
.way-icon{position:absolute;background:var(--blue-tint);border-radius:4px}

/* distribution */
.dist{position:absolute;left:0;top:2182px;width:1200px;height:399px;background:var(--light)}
.dist h2{position:absolute;top:72px;width:100%;text-align:center;color:var(--ink);font-size:22px;font-weight:700}
.dist-col{position:absolute;top:160px;width:190px}
.dist-col h4{display:flex;align-items:center;gap:10px;color:var(--blue);font-size:14px;font-weight:600;margin-bottom:14px}
.dist-col p{font-size:11px;line-height:19px;color:var(--text);height:50px}
.dist-col .btn-dark{position:static;margin-top:12px}

/* split */
.split-blue{position:absolute;left:0;top:2581px;width:600px;height:506px;background:var(--blue)}
.split-photo{left:600px;top:2581px;width:600px;height:506px;background:linear-gradient(120deg,#c9ccd0 0%,#eceeef 40%,#9aa0a6 75%,#5a6066 100%)}
.split-title{position:absolute;left:190px;top:2650px;color:var(--white);font-size:31px;font-weight:700;line-height:46px;width:360px}
.split-sub{position:absolute;left:190px;top:2870px;color:var(--white);font-size:19px;font-weight:600}

/* redemption */
.redeem{left:0;top:3087px;width:1200px;height:585px;background:linear-gradient(135deg,#3a3a3a 0%,#555 45%,#2a2a2a 100%)}
.redeem-shade{position:absolute;left:0;top:3087px;width:1200px;height:585px;background:rgba(0,0,0,.35)}
.redeem-title{position:absolute;left:190px;top:3250px;color:var(--white);font-size:27px;font-weight:700;line-height:43px;width:460px}
.redeem-graphic{left:745px;top:3200px;width:300px;height:262px;background:rgba(255,255,255,.18);border-radius:4px}

/* footer */
.footer{position:absolute;left:0;top:3672px;width:1200px;height:288px;background:var(--footer)}
.foot-col{position:absolute;top:3734px;list-style:none;color:#ddd;font-size:11px;line-height:23px}
.social{position:absolute;left:818px;top:3745px;display:flex;gap:18px}
.social span{width:10px;height:10px;border-radius:50%;background:var(--blue)}
.bottom{position:absolute;left:0;top:3960px;width:1200px;height:31px;background:var(--footer-bar);color:#ccc;font-size:10px;display:flex;align-items:center;justify-content:center}
.bottom em{position:absolute;right:38px;font-style:normal}
</style>
</head>
<body>

<section class="hero">
  <div class="hero-photo" role="img" aria-label="Photo of a business team meeting around laptops in an office"></div>
  <div class="nav"></div>
  <div class="topbar"><span><b>USA OFFICE</b> · PHONE 555-0142</span><span><b>INTERNATIONAL PHONE</b> 1-555-0199</span></div>
  <div class="logo" style="left:160px;top:36px"><i></i>BRIGHTLANE PROMOWORKS</div>
  <nav class="menu">
    <span class="active">HOME</span><span>OUR INCENTIVES</span><span>SAMPLES</span><span>HOW IT WORKS</span><span>TESTIMONIALS</span><span>FAQ</span><span>CONTACT</span><span class="login">LOGIN</span>
  </nav>
  <ul class="stats">
    <li>12 Years In Business</li>
    <li>12,000+ Clients Enrolled</li>
    <li>2+ Million Certificates In Circulation</li>
    <li>170,000 + Redemptions To Date</li>
  </ul>
  <div class="badge"></div>
  <div class="license">Licensed Seller Of Travel (CST #1000000)</div>
  <div class="btn-blue" style="left:210px;top:440px;width:232px;height:42px">30 DAY RISK FREE TRIAL</div>
  <form class="signup">
    <h3>Sign Up Risk Free For 30 Days Right now!</h3>
    <div class="field">Name</div>
    <div class="field">E-Mail</div>
    <div class="field">Phone</div>
    <div class="field">Username</div>
    <div class="btn-blue">SIGN UP NOW</div>
  </form>
  <div class="side-tab">SIGN UP</div>
  <div class="dots" style="left:212px;top:542px"><span class="on"></span><span></span><span></span><span></span></div>
</section>

<h2 class="intro-title">Increase Leads &amp; Sales From Your Existing Marketing Efforts By Offering High Perceived Value Incentives To Your Customers!</h2>
<p class="intro-text">Create a variety giveaway promotions for your business with an unlimited supply of top quality vacation getaway certificates, restaurant giftcertificates, electronic product giveaways and gas or grocery rewards for just $99/mth. Whether you need 100 or 100,000 you will never pay more than $99.</p>
<div class="btn-dark" style="left:208px;top:998px;width:132px;height:42px">Read More</div>
<div class="ph intro-photo" role="img" aria-label="Photo of a person holding a coffee cup working on a laptop"></div>

<div class="band">We Plug Right Into Your<br>Existing Business Model In 4 Ways</div>

<h3 class="way-title" style="left:245px;top:1346px;width:200px">Boost Response Rates To Your Existing Ads</h3>
<p class="way-text" style="left:245px;top:1410px;width:300px">By adding one extra tagline: &quot;Call for a Free Quote and receive a Three Day Two Night Hotel Stay Certificate to Las Vegas or 50 + other popular destinations, No Purchase necessary&quot; &amp; imagine how many more leads you could generate.</p>
<div class="btn-dark sm" style="left:245px;top:1532px">Read More</div>
<div class="way-icon" style="left:638px;top:1345px;width:154px;height:154px" role="img" aria-label="Line illustration of a browser window with a speed gauge"></div>

<div class="way-icon" style="left:308px;top:1627px;width:156px;height:156px" role="img" aria-label="Line illustration of a group of people inside a target crosshair"></div>
<h3 class="way-title" style="left:607px;top:1633px;width:120px">Get More New Customers</h3>
<p class="way-text" style="left:607px;top:1697px;width:300px">Now that you have generated a new lead, try enticing them with an upgrade and offer them Two Nights Plus Airfare if they purchase today.</p>
<div class="btn-dark sm" style="left:607px;top:1773px">Read More</div>

<h3 class="way-title" style="left:245px;top:1897px;width:150px">Increase Repeat &amp; Referral Business</h3>
<p class="way-text" style="left:245px;top:1961px;width:300px">Remind past clients about your products &amp; services with a 7 Night Resort Getaway in one of over 3500 destinations around the world to motivate repeat business and to anyone who fulfills</p>
<div class="btn-dark sm" style="left:245px;top:2058px">Read More</div>
<div class="way-icon" style="left:688px;top:1895px;width:120px;height:152px" role="img" aria-label="Line illustration of connected people profiles above a bar"></div>

<section class="dist">
  <h2>Easy Distribution</h2>
  <div class="dist-col" style="left:170px">
    <h4><svg width="16" height="14" viewBox="0 0 16 14" fill="#151515"><rect x="4" y="0" width="8" height="4"/><rect x="0" y="4" width="16" height="6"/><rect x="4" y="8" width="8" height="6" fill="#fff" stroke="#151515"/></svg>Print</h4>
    <p>Download PDF certificates to print and physically hand them</p>
    <div class="btn-dark sm">Read More</div>
  </div>
  <div class="dist-col" style="left:395px">
    <h4><svg width="16" height="12" viewBox="0 0 16 12" fill="none" stroke="#151515" stroke-width="1.6"><rect x="1" y="1" width="14" height="10"/><path d="M1 1 L8 7 L15 1"/></svg>E-Mail</h4>
    <p>Email e-certificates to your customers individually</p>
    <div class="btn-dark sm">Read More</div>
  </div>
  <div class="dist-col" style="left:608px">
    <h4><svg width="18" height="14" viewBox="0 0 18 14" fill="none" stroke="#151515" stroke-width="1.6"><rect x="1" y="1" width="16" height="9"/><line x1="9" y1="10" x2="9" y2="13"/><line x1="5" y1="13" x2="13" y2="13"/></svg>Online Automation</h4>
    <p>Add our web banners on your website. Your customers</p>
    <div class="btn-dark sm">Read More</div>
  </div>
  <div class="dist-col" style="left:825px">
    <h4><svg width="10" height="16" viewBox="0 0 10 16" fill="none" stroke="#151515" stroke-width="1.6"><rect x="1" y="1" width="8" height="14" rx="1"/><line x1="4" y1="12" x2="6" y2="12"/></svg>SMS</h4>
    <p>Download PDF certificates to print and physically hand them</p>
    <div class="btn-dark sm">Read More</div>
  </div>
</section>

<div class="split-blue"></div>
<div class="ph split-photo" role="img" aria-label="Photo of two men arranging sticky notes on a glass wall"></div>
<h2 class="split-title">Give Away An Unlimited Amount Of Certificates To Your Customers</h2>
<p class="split-sub">For Just $99 Bucks A Month.</p>
<div class="btn-dark" style="left:190px;top:2926px;width:132px;height:42px">Read More</div>

<div class="ph redeem" role="img" aria-label="Dark photo of a desk with a laptop and paper notes"></div>
<div class="redeem-shade"></div>
<h2 class="redeem-title">Completely Separate Redemption Websites - Online Redemption - Online Reservation Requests</h2>
<div class="ph redeem-graphic" role="img" aria-label="Line illustration of a browser window with web address and list items"></div>
<div class="dots" style="left:193px;top:3598px"><span class="on"></span><span></span><span></span></div>

<footer class="footer"></footer>
<div class="logo" style="left:478px;top:3697px"><i></i>BRIGHTLANE PROMOWORKS</div>
<ul class="foot-col" style="left:172px">
  <li>Home</li><li>Our Incentives</li><li>Samples</li><li>How It Works</li><li>Testimonials</li><li>FAQ</li><li>Contact Us</li>
</ul>
<ul class="foot-col" style="left:362px">
  <li>Affiliate Program</li><li>Terms &amp; Conditions</li><li>Privacy Policy</li><li>Login</li>
</ul>
<ul class="foot-col" style="left:545px">
  <li>1840 Harbor View Drive</li><li>Lakemont, CA 90000</li><li>CST-1000000</li><li>Hours: Mon-Fri 7am - 4pm PST</li><li>Sat-Sun CLOSED</li>
</ul>
<div class="social"><span></span><span></span><span></span><span></span></div>
<div class="bottom">© 2017 Company Name &nbsp;|&nbsp; All Rights Reserved<em>CS</em></div>

</body>
</html>
```